Post it Note design

POST-IT NOTE DESIGN (CONTENT)
Size recommended: 4x6 for handwriting space.
Header (Bold):
Lighting Issue Detected on Your Property
Sub-header:
During our routine night inspection, we noted the following item(s):
Checkbox List:
⬜ Building Lights Out
⬜ Pole Lights Out
⬜ Sign Not Illuminated
⬜ Other ________________________
Action Line:
We can provide a quote or dispatch service right away.
Area for notes
Contact Block (Bold & Centered):
Brovane Fixture Inc.
Service@BrovaneFixture.com
www.BrovaneFixture.com
877-514-0862
Industry/Entity Type
Electrical lighting
Colors
Designer to choose colors to be used in the design.
Look and feel
Each slider illustrates characteristics of the customer's brand and the style your logo design should communicate.

```html
<!DOCTYPE html>
<html lang="en">
<head>
<meta charset="UTF-8">
<title>Lighting Issue Detected – Brovane Fixture Inc.</title>
<link rel="stylesheet" href="https://fonts.googleapis.com/css2?family=Lato:wght@400;700;900&family=Montserrat:wght@400;700;800&display=swap">
<style>
  :root {
    --page-bg: #f2f2f2;
    --card-bg: #ffffff;
    --header-bg: #b3cde6;
    --ink: #1c2430;
    --navy: #16202e;
    --frame: #3b4a63;
    --accent-lime: #d4ec3a;
    --dot-line: #7f93c4;
    --action-bg: #e4ecf6;
    --brand-red: #d61f2c;
    --muted: #555c66;
  }
  * { box-sizing: border-box; margin: 0; padding: 0; }
  html, body { width: 1200px; height: 1137px; overflow: hidden; }
  body { background: var(--page-bg); position: relative; font-family: "Lato", sans-serif; color: var(--ink); }

  .note-card {
    position: absolute; left: 265px; top: 83px; width: 660px; height: 987px;
    background: var(--card-bg); box-shadow: 0 2px 8px rgba(0,0,0,.15);
  }

  .note-header { position: absolute; left: 0; top: 0; width: 660px; height: 201px; background: var(--header-bg); }
  .header-photo {
    position: absolute; left: 0; top: 0; width: 245px; height: 201px;
    background: linear-gradient(160deg, #c7d9ec 0%, #a9bfd6 55%, #8ea4b8 100%);
  }
  .headline { position: absolute; left: 276px; top: 36px; width: 345px; text-align: center; font-family: "Montserrat", sans-serif; }
  .headline-top { font-weight: 800; font-size: 38px; letter-spacing: .5px; color: var(--navy); line-height: 44px; }
  .headline-badge {
    display: block; margin: 4px 0 0; height: 45px; background: var(--navy);
    color: var(--accent-lime); font-weight: 800; font-size: 38px; line-height: 45px; letter-spacing: 1px;
  }
  .headline-sub { font-weight: 400; font-size: 35px; color: #3c4452; line-height: 46px; letter-spacing: .5px; }

  .stamp-field {
    position: absolute; top: 219px; width: 290px; height: 41px;
    border: 2px solid var(--frame); font-size: 21px; line-height: 37px; padding-left: 36px;
  }
  .stamp-date { left: 33px; }
  .stamp-time { left: 333px; padding-left: 28px; }

  .intro { position: absolute; left: 32px; top: 280px; width: 600px; font-size: 21px; line-height: 27px; color: #2b323c; }

  .checklist { position: absolute; left: 34px; top: 362px; list-style: none; }
  .checklist li { display: flex; align-items: center; height: 46px; font-size: 25px; color: var(--ink); }
  .check-box { width: 27px; height: 27px; border: 2.5px solid var(--frame); border-radius: 5px; margin-right: 20px; }
  .other-line { display: inline-block; width: 435px; border-bottom: 2px dotted var(--dot-line); margin-left: 8px; transform: translateY(6px); }

  .notes-area {
    position: absolute; left: 38px; top: 558px; width: 591px; height: 147px;
    border: 1.5px solid var(--frame); padding: 34px 25px 0;
  }
  .notes-row { display: flex; gap: 8px; height: 40px; }
  .notes-row span { flex: 1; border-bottom: 2px dotted var(--dot-line); height: 4px; }

  .action-line {
    position: absolute; left: 40px; top: 715px; width: 587px; height: 46px;
    background: var(--action-bg); text-align: center; font-size: 20px; line-height: 46px; color: #222;
  }
  .action-line strong { font-weight: 700; font-size: 21px; }

  .brand-name {
    position: absolute; left: 50px; top: 805px; width: 200px; text-align: center;
    font-family: "Lato", sans-serif; font-weight: 900; font-size: 30px; line-height: 34px; color: var(--brand-red);
  }
  .truck-visual {
    position: absolute; left: 338px; top: 768px; width: 268px; height: 132px;
    background: linear-gradient(180deg, #f3f3f3 0%, #dcdcdc 100%); opacity: .8;
  }

  .contact-bar {
    position: absolute; left: 0; bottom: 0; width: 660px; height: 74px; background: var(--navy);
    display: flex; align-items: center; color: #fff;
  }
  .phone { display: flex; align-items: center; margin-left: 30px; font-weight: 900; font-size: 27px; color: var(--accent-lime); letter-spacing: .5px; }
  .phone svg { margin-right: 14px; }
  .contact-divider { width: 2px; height: 44px; background: var(--brand-red); margin: 0 20px 0 22px; }
  .web-block { font-size: 20px; line-height: 25px; }
</style>
</head>
<body>
  <main class="note-card">
    <header class="note-header">
      <div class="header-photo" role="img" aria-label="Technician in a bucket lift servicing a cluster of parking lot pole lights"></div>
      <h1 class="headline">
        <span class="headline-top">LIGHTING ISSUE</span>
        <span class="headline-badge">DETECTED</span>
        <span class="headline-sub">on Your Property</span>
      </h1>
    </header>

    <div class="stamp-field stamp-date">DATE:</div>
    <div class="stamp-field stamp-time">TIME:</div>

    <p class="intro">During our routine night inspection, we noted the following item(s):</p>

    <ul class="checklist">
      <li><span class="check-box"></span>Building Lights Out</li>
      <li><span class="check-box"></span>Pole Lights Out</li>
      <li><span class="check-box"></span>Sign Not Illuminated</li>
      <li><span class="check-box"></span>Other:<span class="other-line"></span></li>
    </ul>

    <div class="notes-area" aria-label="Notes">
      <div class="notes-row"><span></span><span></span></div>
      <div class="notes-row"><span></span><span></span></div>
      <div class="notes-row"><span></span><span></span></div>
    </div>

    <p class="action-line">We can provide a <strong>quote or dispatch service</strong> right away.</p>

    <div class="brand-name">Brovane Fixture Inc.</div>
    <div class="truck-visual" role="img" aria-label="Faded service bucket truck"></div>

    <footer class="contact-bar">
      <div class="phone">
        <svg width="30" height="30" viewBox="0 0 30 30" aria-hidden="true">
          <circle cx="15" cy="15" r="13" fill="none" stroke="#d4ec3a" stroke-width="2.2"/>
          <path d="M10.5 8.5c-.8.6-1.5 1.7-1 3.3 1 3.3 4.5 7.2 7.8 8.5 1.5.6 2.6 0 3.3-.8l.6-.8-2.8-2.1-1.3 1.2c-1.7-.7-3.6-2.7-4.3-4.4l1.2-1.3-2-2.8z" fill="#d4ec3a"/>
        </svg>
        877-514-0862
      </div>
      <div class="contact-divider"></div>
      <div class="web-block">
        <div>Service@BrovaneFixture.com</div>
        <div>www.BrovaneFixture.com</div>
      </div>
    </footer>
  </main>
</body>
</html>
```